Business Card for Freelance Copywriting & Web Design Business

Hi! I have a logo but want a new business card. Here's a better idea of what I'm thinking:
-Brand new double-sided business card, rounded cards, embossed logo, nice quality paper
-Include phone (604-382-5194), email (hello@lauraberndt.org), and website (www.lauraberndt.org). No address, please, since I service clients worldwide.
-I'd like the fonts to match those on my website (www.lauraberndt.org). I had to purchase the one font (Born Ready), attached. I'm not sure which version was used on my site so I included all that I purchased. The secondary font is Helvetica
-I'd also like the tagline "Powerful Words. Impressive Results." included.
-My primary brand colour is the teal, colour #19ADC3
Laura Berndt | Laura Berndt Copywriting & Web Design <hello@lauraberndt.org>
-I'd also like the following services listed on the new cards:
SEO Website Content
SEO Blog Content
SEO Website Design
Contact Information for Business Card
as stated in brief
Font styles to use
Other font styles liked:
- See brief
Look and feel
Each slider illustrates characteristics of the customer's brand and the style your logo design should communicate.

```html
<!DOCTYPE html>
<html lang="en">
<head>
<meta charset="utf-8">
<title>Laura Berndt – Business Card</title>
<link rel="stylesheet" href="https://fonts.googleapis.com/css2?family=Montserrat:wght@400;500;700&display=swap">
<style>
  :root {
    --teal: #19adc3;
    --ink: #1a1a1a;
    --card-dark: #181818;
    --paper: #ffffff;
    --backdrop: #3a3a3a;
    --emboss: #2e2e2e;
    --light-text: #f2f2f2;
  }
  * { box-sizing: border-box; margin: 0; padding: 0; }
  html, body { width: 1200px; height: 1059px; overflow: hidden; }
  body {
    background: var(--backdrop);
    position: relative;
    font-family: "Montserrat", Helvetica, Arial, sans-serif;
  }
  .card {
    position: absolute;
    width: 690px;
    height: 393px;
    border-radius: 18px;
    overflow: hidden;
    box-shadow: 0 14px 28px rgba(0,0,0,.45);
  }
  .card--front { left: 256px; top: 100px; background: var(--paper); }
  .card--back { left: 253px; top: 537px; background: var(--card-dark); }

  .front__swoosh { position: absolute; left: 0; top: 0; width: 690px; height: 393px; }

  .brand-mark {
    position: absolute;
    left: 56px; top: 158px;
    width: 260px;
    display: flex; align-items: center; gap: 10px;
    font-weight: 500;
    font-size: 27px;
    color: var(--ink);
    white-space: nowrap;
  }
  .brand-mark__dot {
    width: 14px; height: 14px; border-radius: 50%;
    background: var(--teal); flex: none;
  }

  .front__divider {
    position: absolute; left: 343px; top: 76px;
    width: 2px; height: 213px; background: var(--teal);
  }
  .front__details { position: absolute; left: 378px; top: 68px; color: var(--ink); }
  .details__name {
    font-weight: 700; font-size: 32px; color: var(--teal);
    line-height: 1; letter-spacing: .2px;
  }
  .details__role { font-size: 16px; margin-top: 8px; letter-spacing: .3px; }
  .details__tagline { font-size: 16px; margin-top: 22px; line-height: 20px; letter-spacing: .3px; }
  .details__contacts { list-style: none; margin-top: 26px; }
  .details__contacts li {
    display: flex; align-items: center; gap: 8px;
    font-size: 16px; height: 27.5px; letter-spacing: .3px;
  }
  .details__contacts svg { width: 13px; height: 13px; flex: none; }

  .back__mark {
    position: absolute; left: 0; right: 0; top: 160px;
    text-align: center;
    font-weight: 500; font-size: 64px;
    color: var(--emboss);
    white-space: nowrap;
  }
  .back__services {
    position: absolute; left: 0; right: 0; top: 337px;
    text-align: center;
    font-size: 16.5px; color: var(--light-text); letter-spacing: .3px;
    white-space: nowrap;
  }
  .back__services .sep {
    display: inline-block; width: 6px; height: 6px; border-radius: 50%;
    background: var(--teal); margin: 0 9px; vertical-align: middle;
  }
</style>
</head>
<body>

<section class="card card--front" aria-label="Business card front">
  <svg class="front__swoosh" viewBox="0 0 690 393" aria-hidden="true">
    <path d="M0 320 Q170 370 340 366 Q520 362 690 320 L690 393 L0 393 Z" fill="var(--card-dark)"/>
    <path d="M200 352 Q470 360 690 289 L690 303 Q470 368 200 352 Z" fill="var(--teal)"/>
    <path d="M210 358 Q480 372 690 307 L690 317 Q480 380 210 358 Z" fill="var(--teal)"/>
  </svg>

  <div class="brand-mark">
    <span class="brand-mark__dot"></span>
    <span>Laura Berndt</span>
  </div>

  <div class="front__divider"></div>

  <div class="front__details">
    <h1 class="details__name">Laura Berndt</h1>
    <p class="details__role">Copywriting &amp; Web Designer</p>
    <p class="details__tagline">Powerful Words.<br>Impressive Results.</p>
    <ul class="details__contacts">
      <li>
        <svg viewBox="0 0 16 16" aria-hidden="true"><path d="M3 1l3 3-1.5 2c1 2 3 4 5 5L11.5 9.5l3 3-2 2.5C7 14 2 9 1 3z" fill="var(--teal)"/></svg>
        <span>604-382-5194</span>
      </li>
      <li>
        <svg viewBox="0 0 16 16" aria-hidden="true"><rect x="1" y="3" width="14" height="10" fill="var(--teal)"/><path d="M1 3l7 6 7-6" stroke="#fff" stroke-width="1.3" fill="none"/></svg>
        <span>hello@lauraberndt.org</span>
      </li>
      <li>
        <svg viewBox="0 0 16 16" aria-hidden="true" fill="none" stroke="var(--teal)" stroke-width="1.3"><circle cx="8" cy="8" r="6.5"/><ellipse cx="8" cy="8" rx="3" ry="6.5"/><path d="M1.5 8h13M2.5 4.5h11M2.5 11.5h11"/></svg>
        <span>www.lauraberndt.org</span>
      </li>
    </ul>
  </div>
</section>

<section class="card card--back" aria-label="Business card back">
  <div class="back__mark">Laura Berndt</div>
  <p class="back__services">
    SEO Website Content<span class="sep"></span>SEO Blog Content<span class="sep"></span>SEO Website Design
  </p>
</section>

</body>
</html>
```